A Maple Syrup Label for a Local Buniness

We are looking for a label for our maple syrup business. Our business currently sells honey, and we are expanding into maple syrup. Our Business name is "Brackley Honey" and we currently have a logo attached below. We would like to incorporate the bee and BH part, but the label could also read "Brackley Farms" with the words maple syrup. We do not want consumers to confuse the maple syrup jars with the honey jars. It should be clear that the jars contain maple syrup. We are open to new designs as well.

```html
<!DOCTYPE html>
<html lang="en">
<head>
<meta charset="utf-8">
<title>Brackley Honey – Maple Syrup Label</title>
<link rel="stylesheet" href="https://fonts.googleapis.com/css2?family=Montserrat:ital,wght@0,600;0,700;1,700&family=Oswald:wght@700&family=Open+Sans:wght@400&display=swap">
<style>
  :root {
    --bg: #ffffff;
    --label-cream: #fdf0df;
    --label-white: #ffffff;
    --ring-yellow: #f8be12;
    --ink: #111111;
    --ink-soft: #2b2b2b;
    --gold-dark: #c9a046;
    --gold-light: #f3dd95;
  }
  html, body {
    margin: 0;
    padding: 0;
    width: 1200px;
    height: 993px;
    overflow: hidden;
    background: var(--bg);
  }
  .canvas {
    width: 1200px;
    height: 993px;
    display: block;
  }
  .arc-heading {
    font-family: "Montserrat", sans-serif;
    font-weight: 700;
    font-size: 34px;
    letter-spacing: 3px;
    fill: var(--ink);
  }
  .brand-name {
    font-family: "Montserrat", sans-serif;
    font-weight: 700;
    font-size: 52px;
    letter-spacing: 1px;
    fill: var(--ink);
  }
  .product-title {
    font-family: "Oswald", sans-serif;
    font-weight: 700;
    font-size: 96px;
    fill: var(--ink);
  }
  .farm-name {
    font-family: "Montserrat", sans-serif;
    font-weight: 700;
    font-style: italic;
    font-size: 33px;
    fill: var(--ink-soft);
  }
  .purity {
    font-family: "Open Sans", sans-serif;
    font-weight: 400;
    font-size: 27px;
    fill: var(--ink-soft);
  }
</style>
</head>
<body>
<svg class="canvas" viewBox="0 0 1200 993" xmlns="http://www.w3.org/2000/svg">
  <defs>
    <radialGradient id="label-fill" cx="0.5" cy="0.6" r="0.6">
      <stop offset="0" stop-color="var(--label-white)"/>
      <stop offset="0.7" stop-color="#fffaf3"/>
      <stop offset="1" stop-color="var(--label-cream)"/>
    </radialGradient>
    <linearGradient id="gold-rule" x1="0" y1="0" x2="1" y2="0">
      <stop offset="0" stop-color="var(--gold-dark)"/>
      <stop offset="0.5" stop-color="var(--gold-light)"/>
      <stop offset="1" stop-color="var(--gold-dark)"/>
    </linearGradient>
    <path id="heading-arc" d="M 425 262 A 200 175 0 0 1 775 262"/>
  </defs>

  <g class="label">
    <ellipse class="label-body" cx="600" cy="496" rx="340" ry="450" fill="url(#label-fill)"/>
    <ellipse class="label-ring" cx="600" cy="496" rx="312" ry="420" fill="none" stroke="var(--ring-yellow)" stroke-width="24"/>

    <text class="arc-heading">
      <textPath href="#heading-arc" startOffset="50%" text-anchor="middle">ORGANIC FARM</textPath>
    </text>

    <g class="brand-mark">
      <circle cx="600" cy="330" r="16" fill="var(--ring-yellow)"/>
      <text class="brand-name" x="600" y="430" text-anchor="middle">BRACKLEY</text>
      <text class="brand-name" x="600" y="492" text-anchor="middle">HONEY</text>
    </g>

    <text class="product-title" x="600" y="652" text-anchor="middle" textLength="472" lengthAdjust="spacingAndGlyphs">MAPLE SYRUP</text>

    <line class="gold-rule" x1="418" y1="688" x2="782" y2="688" stroke="url(#gold-rule)" stroke-width="6" stroke-linecap="round"/>
    <text class="farm-name" x="600" y="732" text-anchor="middle">Brackley Farms</text>
    <line class="gold-rule" x1="418" y1="756" x2="782" y2="756" stroke="url(#gold-rule)" stroke-width="6" stroke-linecap="round"/>

    <text class="purity" x="600" y="806" text-anchor="middle">100% PURE</text>
  </g>
</svg>
</body>
</html>
```